Cover für Gedichtbuch
Zielgruppe
Das Buch soll jungen und alten Menschen gefallen. Zielgruppe sind aber vor allem junge Leser zwischen 18 und Mitte 20.
Aufgabenstellung
Für das Erstlingswerk von zwei Nachwuchsautoren wird ein Wendecover gesucht. Sprich: Auf der einen Seite stehen Gedichte mit hellen Gedichten (Liebe, Freude, Glück) - die andere Hälfte besteht aus dunklen Gedichten (Tod, Depression). Das Buch soll gedreht werden. Daher sollen die beiden Coverseiten einen Kontrast darstellen.

```html
<!DOCTYPE html>
<html lang="de">
<head>
<meta charset="utf-8">
<title>helle Gedichte · dunkle Gedichte – Wendecover</title>
<link rel="stylesheet" href="https://fonts.googleapis.com/css2?family=Sorts+Mill+Goudy&display=swap">
<style>
  :root {
    --paper: #ffffff;
    --ink: #000000;
    --light-mid: #b4b4b4;
    --dark-mid: #a8a8a8;
    --dark-deep: #1a1a1a;
    --title-light: #ffffff;
    --title-dark: #d2d2d2;
    --shadow-soft: rgba(0, 0, 0, 0.5);
    --shadow-hard: rgba(0, 0, 0, 0.85);
  }
  html, body {
    margin: 0;
    padding: 0;
    width: 1200px;
    height: 845px;
    overflow: hidden;
    background: var(--paper);
  }
  .reversible-cover {
    position: relative;
    width: 1200px;
    height: 845px;
    background: var(--paper);
    font-family: "Sorts Mill Goudy", "Goudy Old Style", serif;
  }
  .cover-side {
    position: absolute;
    top: 0;
    height: 845px;
    overflow: hidden;
  }
  .cover-side--light {
    left: 0;
    width: 592px;
    background: linear-gradient(180deg,
      var(--paper) 0%,
      #e4e4e4 10%,
      var(--light-mid) 22%,
      #bdbdbd 45%,
      #8a8a8a 56%,
      #1c1c1c 66%,
      #555 76%,
      #cfcfcf 86%,
      var(--paper) 94%);
  }
  .cover-side--dark {
    left: 606px;
    width: 594px;
    background: linear-gradient(180deg,
      var(--ink) 0%,
      #111 7%,
      #7a7a7a 18%,
      #f2f2f2 27%,
      var(--dark-mid) 42%,
      #c4c4c4 56%,
      #f0f0f0 66%,
      #9a9a9a 76%,
      #3a3a3a 86%,
      var(--dark-deep) 94%,
      var(--ink) 100%);
  }
  .artwork {
    position: absolute;
  }
  .artwork--tree-manuscript {
    left: 0;
    top: 170px;
    width: 592px;
    height: 560px;
    background: radial-gradient(ellipse at 55% 45%,
      rgba(255, 255, 255, 0.55) 0%,
      rgba(220, 220, 220, 0.35) 45%,
      rgba(255, 255, 255, 0) 75%);
  }
  .artwork--roots-manuscript {
    left: 0;
    top: 60px;
    width: 594px;
    height: 620px;
    background: radial-gradient(ellipse at 45% 45%,
      rgba(60, 60, 60, 0.35) 0%,
      rgba(90, 90, 90, 0.2) 45%,
      rgba(0, 0, 0, 0) 75%);
  }
  .cover-word {
    position: absolute;
    margin: 0;
    font-weight: 400;
    line-height: 1;
    white-space: nowrap;
  }
  .cover-side--light .cover-word {
    color: var(--title-light);
    text-shadow: 3px 5px 6px var(--shadow-soft), 0 0 2px rgba(0, 0, 0, 0.35);
  }
  .cover-side--dark .cover-word {
    color: var(--title-dark);
    text-shadow: -3px -5px 6px var(--shadow-hard), 0 0 2px rgba(0, 0, 0, 0.6);
    transform: rotate(180deg);
  }
  .cover-side--light .cover-word--mood {
    font-size: 262px;
    letter-spacing: -1px;
    left: -20px;
    top: -14px;
  }
  .cover-side--light .cover-word--genre {
    font-size: 235px;
    letter-spacing: 1px;
    left: 134px;
    top: 282px;
  }
  .cover-side--dark .cover-word--genre {
    font-size: 235px;
    letter-spacing: 1px;
    left: 12px;
    top: 291px;
  }
  .cover-side--dark .cover-word--mood {
    font-size: 160px;
    letter-spacing: 12px;
    left: 34px;
    top: 658px;
  }
</style>
</head>
<body>
  <main class="reversible-cover">
    <section class="cover-side cover-side--light" aria-label="Vorderseite: helle Gedichte">
      <div class="artwork artwork--tree-manuscript" role="img" aria-label="Heller Baum als weiße Silhouette über einer handgeschriebenen Manuskriptseite"></div>
      <h1 class="cover-word cover-word--mood">helle</h1>
      <p class="cover-word cover-word--genre">Gedichte</p>
    </section>
    <section class="cover-side cover-side--dark" aria-label="Rückseite: dunkle Gedichte">
      <div class="artwork artwork--roots-manuscript" role="img" aria-label="Dunkles Wurzelwerk über einer handgeschriebenen Manuskriptseite"></div>
      <p class="cover-word cover-word--genre" aria-label="Gedichte">chte</p>
      <h2 class="cover-word cover-word--mood">dunkle</h2>
    </section>
  </main>
</body>
</html>
```